Zuteno is an ethnic owned company passionate about the CBD and cannabis industry.

*we are using amber colored bottles with white and gold lids*
Here are the dimensions of the bottles.
2 oz
4 ¼ inch Height
1 ¼ inch Diameter
4 inch Circumference
20/410 Neck Size

8 oz
186 mm Height
47 mm Diameter
24/410 Neck Size

On the front label we would like to add “Your wellness starts within”
Shampoo ingredients
Ingredients: Water Biotin Vitamin D3 (Cholecaliferol) Powder Decyl Glucoside Sulfosuccinate Coco Betaine Citric Acid Vegetable Glycerin Xanthan Gum Aloe Vera Pure Juice Horestail Extract Nettle Extract Saw Palmetto Extract Gingko Biloba Zinc PCA Honeyquat Peppermint EO Tea Tree EO Phenoxehtanol SA Vitamin B5 (D-Panthenol) CBD: Isolate MCT Oil Polysorbate 80

Shampoo How To Use: Apply a generous amount to the scalp and work toward the ends. Rinse thoroughly with cool water.
For best results, use in conjuction
with Zuteno CBD Conditioner.

Warning: For external use only, Avoid direct contact with eyes and mouth. Not intended for use by anyone under the age of 18 without adult supervision. Do not use if you are pregnant or nursing. Consult your physician prior to use if you are taking any medications. If any adverse reactions occur, discontinue use and consult your doctor.

This product contains a total delta-9-THC concentration that does not exceed 0.3% on a dry-weight basis. It is the customer’s responsibility to know applicable state and local laws in regard to use of this product.

*These statements have not been evaluated
by the Bureau of Tonic Oversight. This
product is not intended to diagnose, treat,
cure or prevent any disease.

ZUTENO COMPANY 417 ROUTE 52 #20391
TRENTON NJ 08917
ZUTENOCOMPANY.EXAMPLE

*PLEASE ADD PROUDLY MADE IN THE USA SYMBOL AND RECYCLE SYMBOL*

Conditioner ingredients
Ingredients: Water Jojoba Oil Avocado Oil Grapeseed oil Argan Oil MCT Oil CBD: Isolate BTMS 50 Shea Butter Cetearyl Alchohol Lavender EO Peppermint EO Aloe Vera Pure Juice Honeyquat Phenoxehtanol SA Vitamin B5 (D-Panthenol)

Conditioner HOW TO USE: Apply to wet hair and gently lather with fingertips. Rinse and repeat. Leave on 5 minutes. For the best results.

WARNING: Consult your healthcare provider if you’re nursing, pregnant, or taking medication. If adverse reactions occur, discontinue use and consult your physician. Keep ou
t of the reach of children.

TRENTON NJ 08917
ZUTENOCOMPANY.EXAMPLE

WE ALSO NEED A QR CODE PLACED ON THE BACK TO OUR SITE.

*PLEASE ADD PROUDLY MADE IN THE USA SYMBOL, RECYCLE SYMBOL, MINORITY OWNED BUSINESS*

Requirements
Must have
• *PLEASE USE COLOR PALETTE IN PHOTOS*
*We would like a black background for the label*
*The word CBD and the mg of CBD in each shampoo bottle size, 8 oz bottle 250 mg of CBD and 60 mg of CBD for the 2 oz bottle*
*We need two designs. One with set with CBD advertised on the bottles and one without for advertising and social media reasons!*
Should not have
• Cannabis leaves, the word hemp,

```html
<!DOCTYPE html>
<html lang="en">
<head>
<meta charset="utf-8">
<title>Zuteno Shampoo &amp; Conditioner Labels</title>
<link rel="stylesheet" href="https://fonts.googleapis.com/css2?family=Barlow+Condensed:wght@400;500;600&family=Josefin+Sans:wght@300&display=swap">
<style>
  :root {
    --backdrop: #3a3a3b;
    --paper: #ffffff;
    --paper-shade: #f1f2f1;
    --green-dark: #4f6b56;
    --green-light: #9cb69e;
    --green-type: #8cab90;
    --green-mark: #6f9275;
    --ink: #4b4b4b;
    --ink-head: #3f5e47;
  }
  * { margin: 0; padding: 0; box-sizing: border-box; }
  html, body { width: 1187px; height: 1200px; overflow: hidden; background: var(--backdrop); }
  .sheet { position: relative; width: 1187px; height: 1200px; }

  .label {
    position: absolute; top: 216px; width: 540px; height: 767px;
    background: var(--paper); display: flex;
    box-shadow: 0 6px 14px rgba(0,0,0,.45);
    font-family: "Barlow Condensed", sans-serif;
  }
  .label--shampoo { left: 33px; }
  .label--conditioner { left: 614px; }

  .panel { position: relative; height: 100%; }
  .panel--front { width: 270px; }
  .panel--back { width: 270px; background: linear-gradient(90deg, var(--paper-shade) 0%, var(--paper) 22%); }

  .band { position: absolute; left: 0; right: 0; }
  .band--top { top: 0; height: 39px; }
  .band--bottom { bottom: 36px; height: 36px; }
  .band--dark { background: var(--green-dark); }
  .band--light { background: var(--green-light); }

  .brand {
    position: absolute; top: 160px; left: 0; width: 100%; text-align: center;
    font-family: "Josefin Sans", sans-serif; font-weight: 300;
    font-size: 24px; letter-spacing: 7px; color: var(--green-mark);
  }
  .product-name {
    position: absolute; bottom: 88px;
    writing-mode: vertical-rl; transform: rotate(180deg);
    font-weight: 500; color: var(--green-type); line-height: .8;
  }
  .label--shampoo .product-name { left: 112px; font-size: 146px; }
  .label--conditioner .product-name { left: 118px; font-size: 94px; }
  .volume {
    position: absolute; left: 25px; bottom: 88px;
    font-size: 28px; font-weight: 500; color: var(--ink); line-height: 1;
  }

  .copy {
    position: absolute; left: 32px; width: 212px;
    font-size: 11.4px; line-height: 14.6px; color: var(--ink);
  }
  .label--shampoo .copy { top: 62px; }
  .label--conditioner .copy { top: 166px; }
  .copy p { margin-bottom: 9px; }
  .copy strong { font-weight: 600; color: var(--ink-head); }

  .marks { position: absolute; left: 32px; top: 632px; display: flex; align-items: center; gap: 34px; }
  .recycle { width: 74px; height: 70px; }
  .origin-seal { width: 70px; height: 70px; border-radius: 50%; background: var(--green-dark); border: 4px solid var(--green-light); }
</style>
</head>
<body>
<main class="sheet">

  <section class="label label--shampoo">
    <div class="panel panel--front">
      <div class="band band--top band--dark"></div>
      <div class="brand">ZUTENO</div>
      <div class="product-name">SHAMPOO</div>
      <div class="volume">8 oz</div>
      <div class="band band--bottom band--light" style="bottom:0"></div>
    </div>
    <div class="panel panel--back">
      <div class="band band--top band--light"></div>
      <div class="copy">
        <p><strong>INGREDIENTS:</strong> Water Biotin Vitamin D3 (Cholecaliferol) Powder Decyl Glucoside Sulfosuccinate Coco Betaine Citric Acid Vegetable Glycerin Xanthan Gum Aloe Vera Pure Juice Horestail Extract Nettle Extract Saw Palmetto Extract Gingko Biloba Zinc PCA Honeyquat Peppermint EO Tea Tree EO Phenoxehtanol SA Vitamin B5 (D-Panthenol) CBD: Isolate MCT Oil Polysorbate 80</p>
        <p><strong>HOW TO USE:</strong> Apply a generous amount to the scalp and work toward the ends. Rinse thoroughly with cool water.<br>For best results, use in conjuction<br>with Zuteno CBD Conditioner.</p>
        <p><strong>WARNING:</strong> For external use only, Avoid direct contact with eyes and mouth. Not intended for use by anyone under the age of 18 without adult supervision. Do not use if you are pregnant or nursing. Consult your physician prior to use if you are taking any medications. If any adverse reactions occur, discontinue use and consult your doctor.</p>
        <p>This product contains a total delta-9-THC concentration that does not exceed 0.3% on a dry-weight basis. It is the customer’s responsibility to know applicable state and local laws in regard to use of this product.</p>
        <p>*These statements have not been evaluated by the Bureau of Tonic Oversight. This product is not intended to diagnose, treat, cure or prevent any disease.</p>
        <p>ZUTENO COMPANY 417 ROUTE 52 #20391<br>TRENTON NJ 08917<br>ZUTENOCOMPANY.EXAMPLE</p>
      </div>
      <div class="marks">
        <svg class="recycle" viewBox="0 0 74 70" role="img" aria-label="Recycle symbol">
          <g fill="none" stroke="var(--green-dark)" stroke-width="9" stroke-linejoin="round">
            <path d="M28 12 L18 30"/><path d="M46 12 L56 30"/><path d="M14 48 L60 48"/>
          </g>
          <g fill="var(--green-light)">
            <path d="M30 4 L48 4 L38 20 Z"/><path d="M8 36 L24 26 L22 48 Z"/><path d="M66 36 L52 58 L68 56 Z"/>
          </g>
        </svg>
        <div class="origin-seal" role="img" aria-label="Made in the USA seal"></div>
      </div>
      <div class="band band--bottom band--dark" style="bottom:0"></div>
    </div>
  </section>

  <section class="label label--conditioner">
    <div class="panel panel--front">
      <div class="band band--top band--dark"></div>
      <div class="brand">ZUTENO</div>
      <div class="product-name">CONDITIONER</div>
      <div class="volume">8 oz</div>
      <div class="band band--bottom band--light" style="bottom:0"></div>
    </div>
    <div class="panel panel--back">
      <div class="band band--top band--light"></div>
      <div class="copy">
        <p><strong>INGREDIENTS:</strong> Ingredients: Water Jojoba Oil Avocado Oil Grapeseed oil Argan Oil MCT Oil CBD: Isolate BTMS 50 Shea Butter Cetearyl Alchohol Lavender EO Peppermint EO Aloe Vera Pure Juice Honeyquat Phenoxehtanol SA Vitamin B5 (D-Panthenol)</p>
        <p><strong>HOW TO USE:</strong> Apply to wet hair and gently lather with fingertips. Rinse and repeat. Leave on 5 minutes. For the best results.</p>
        <p><strong>WARNING:</strong> Consult your healthcare provider if you’re nursing, pregnant, or taking medication. If adverse reactions occur, discontinue use and consult your physician. Keep ou<br>t of the reach of children.</p>
        <p>This product contains a total delta-9-THC concentration that does not exceed 0.3% on a dry-weight basis. It is the customer’s responsibility to know applicable state and local laws in regard to use of this product.</p>
        <p>*These statements have not been evaluated by the Bureau of Tonic Oversight. This product is not intended to diagnose, treat, cure or prevent any disease.</p>
        <p>ZUTENO COMPANY 417 ROUTE 52 #20391<br>TRENTON NJ 08917<br>ZUTENOCOMPANY.EXAMPLE</p>
      </div>
      <div class="marks">
        <svg class="recycle" viewBox="0 0 74 70" role="img" aria-label="Recycle symbol">
          <g fill="none" stroke="var(--green-dark)" stroke-width="9" stroke-linejoin="round">
            <path d="M28 12 L18 30"/><path d="M46 12 L56 30"/><path d="M14 48 L60 48"/>
          </g>
          <g fill="var(--green-light)">
            <path d="M30 4 L48 4 L38 20 Z"/><path d="M8 36 L24 26 L22 48 Z"/><path d="M66 36 L52 58 L68 56 Z"/>
          </g>
        </svg>
        <div class="origin-seal" role="img" aria-label="Made in the USA seal"></div>
      </div>
      <div class="band band--bottom band--dark" style="bottom:0"></div>
    </div>
  </section>

</main>
</body>
</html>
```